Wavelume artwork for new single release

I need Wavelume artwork creating to release a new single on there.

The specs are:

Ideal size: 3000 x 3000 pixels
Minimum size: 1400 x 1400 pixels
Aspect ratio: 1:1 (must be a perfect square)
File format: JPG or PNG
Color space: sRGB
File size: Max 4MB

The song is called "Still, Can We Wander?"
The artist is "Milo Fenwright"

We have no images of Milo, so it really is open to imagination.

Target Market(s)

Wavelume listeners

Industry/Entity Type

Music

```html
<!DOCTYPE html>
<html lang="en">
<head>
<meta charset="utf-8">
<title>Still, Can We Wander? — Milo Fenwright single cover</title>
<link rel="stylesheet" href="https://fonts.googleapis.com/css2?family=Playfair+Display:wght@500&family=Yellowtail&family=Montserrat:wght@600&display=swap">
<style>
  :root {
    --plum-deep: #2b1830;
    --plum: #3a1c33;
    --wine: #6e2034;
    --crimson: #a62b3b;
    --rose: #b34452;
    --ember: #e0714c;
    --glow: #f4a566;
    --gold: #f2b560;
    --peach: #f6b98a;
    --white: #ffffff;
  }
  html, body {
    margin: 0;
    padding: 0;
    width: 1200px;
    height: 1200px;
    overflow: hidden;
    background: var(--plum-deep);
  }
  .single-cover {
    position: relative;
    width: 1200px;
    height: 1200px;
    overflow: hidden;
    background:
      linear-gradient(180deg, var(--plum-deep) 0%, var(--plum) 22%, var(--wine) 52%, var(--crimson) 82%, var(--rose) 100%);
  }
  .single-cover__glow {
    position: absolute;
    left: 600px;
    top: 661px;
    width: 1000px;
    height: 1000px;
    transform: translate(-50%, -50%);
    border-radius: 50%;
    background: radial-gradient(circle, rgba(244,165,102,0.85) 0%, rgba(224,113,76,0.55) 30%, rgba(166,43,59,0.25) 55%, rgba(166,43,59,0) 72%);
  }
  .single-cover__title {
    position: absolute;
    top: 92px;
    left: 0;
    width: 1200px;
    margin: 0;
    text-align: center;
    white-space: nowrap;
    font-family: "Playfair Display", serif;
    font-weight: 500;
    font-size: 100px;
    letter-spacing: -3px;
    color: var(--white);
    line-height: 1.3;
  }
  .single-cover__title-script {
    font-family: "Yellowtail", cursive;
    font-size: 128px;
    letter-spacing: 0;
    color: var(--peach);
    padding: 0 6px;
    position: relative;
    top: 10px;
    text-shadow: 2px 4px 6px rgba(40, 10, 20, 0.45);
  }
  .single-cover__emblem {
    position: absolute;
    left: 220px;
    top: 281px;
    width: 760px;
    height: 760px;
  }
  .single-cover__artist {
    position: absolute;
    top: 1086px;
    left: 0;
    width: 1200px;
    margin: 0;
    text-align: center;
    font-family: "Montserrat", sans-serif;
    font-weight: 600;
    font-size: 38px;
    letter-spacing: 0.48em;
    text-indent: 0.48em;
    color: var(--white);
  }
</style>
</head>
<body>
  <main class="single-cover">
    <div class="single-cover__glow"></div>

    <h1 class="single-cover__title">Still, Can We <span class="single-cover__title-script">Wander</span>?</h1>

    <svg class="single-cover__emblem" viewBox="0 0 760 760" xmlns="http://www.w3.org/2000/svg">
      <defs>
        <radialGradient id="heart-fill" cx="50%" cy="45%" r="55%">
          <stop offset="0%" stop-color="#8a2a45"/>
          <stop offset="100%" stop-color="#4e1a35"/>
        </radialGradient>
      </defs>
      <circle class="emblem-ring" cx="380" cy="380" r="314" fill="none" stroke="var(--gold)" stroke-width="5"/>
      <circle class="emblem-art" cx="380" cy="380" r="270" fill="url(#heart-fill)" opacity="0.85"
              role="img" aria-label="Illustration of a cracked heart with glowing gold fracture lines inside a fine geometric halo"/>
    </svg>

    <p class="single-cover__artist">MILO FENWRIGHT</p>
  </main>
</body>
</html>
```